Penny auction website for high end market

need a penny auction web design , requirement as below :-

- classy and noble, as i am only selli high end products
- 25 products for the main page , 5 products per row ( please see sample picture )
- top 5 products can be highlighted as those are limited edition products
- main page , products page, members page , faq and about us page
- matching logo with the name lotvo
- clean
- responsive for desktoop
-mobile version
Updates

i missed the mobile version, i should get the mobile version aswell, for desktop it should be responsive Added Wednesday, August 16, 2017

designer may use gold or silver color too as i am selling only high end products exclusively for members only, the layout can be different than the sample, it just a guide line for the sample, other better layout would be great to see and to have.

some idea how highend feel to me https://img.kravenstock.example/scr/51200/shimmering-gem-layout-template_51277-original.jpg

guys, please use this design https://www.layoutquarry.example/site-templates/51277.html as the base , i want it high class and up market, thanks

Target Market(s)

highend products buyer

Number of Pages Required

5+ page

Font styles to use
Serif
Sans Serif
Script
Other font styles liked:
• designer match it

Colors

Designer to choose colors to be used in the design.

Requirements
Must have
• source code, logos ( use lotvo for now, will change later when confirm ) , PSD
Nice to have
• more different type of designs would be great, designers can present they ideas other than my requirement

```html
<!DOCTYPE html>
<html lang="en">
<head>
<meta charset="utf-8">
<title>lotvo — Penny Auctions</title>
<link href="https://fonts.googleapis.com/css2?family=Roboto:wght@400;500;700&family=Roboto+Condensed:wght@700&display=swap" rel="stylesheet">
<style>
:root{
  --gold:#ab9e78;
  --gold-dark:#9a8d68;
  --ink:#333333;
  --line:#e6e6e6;
  --topbar:#f1f1f1;
  --cream:#f4f1ea;
  --footer:#2c2c2c;
  --footer-text:#bdbdbd;
  --white:#ffffff;
  --black:#0d0d0d;
}
*{box-sizing:border-box;margin:0;padding:0}
html,body{width:1200px;height:2535px;overflow:hidden}
body{font-family:"Roboto",Arial,sans-serif;color:var(--ink);background:var(--white);position:relative}
a{color:inherit;text-decoration:none}
ul{list-style:none}

/* top bar */
.topbar{height:30px;background:var(--topbar);display:flex;align-items:center;justify-content:space-between;padding:0 160px}
.social{display:flex;gap:6px}
.social span{width:19px;height:19px;border-radius:50%;background:#dcdcdc;display:block}
.account-links{display:flex;font-size:10px;text-transform:uppercase;color:#555}
.account-links a{padding:0 10px;border-left:1px solid #bbb;line-height:10px}
.account-links a:first-child{border-left:0}
.account-links a:last-child{padding-right:0}

/* header */
.header{height:75px;display:flex;align-items:center;justify-content:space-between;padding:0 160px}
.brand{display:flex;align-items:center;gap:10px}
.brand-dot{width:14px;height:14px;background:var(--gold);display:block}
.brand-name{font-size:32px;font-weight:500;color:var(--ink);letter-spacing:.5px}
.search{display:flex;width:503px;height:38px}
.search input{flex:1;border:1px solid #ddd;border-right:0;padding:0 12px;font:11px "Roboto",sans-serif;color:#999}
.search button{width:61px;border:0;background:var(--gold);display:flex;align-items:center;justify-content:center}

/* nav */
.nav{height:48px;background:var(--gold);display:flex;justify-content:space-between;padding:0 160px}
.nav ul{display:flex}
.nav li a{display:flex;align-items:center;height:48px;padding:0 17px;font-size:11px;font-weight:400;color:var(--white);text-transform:uppercase}
.nav li.active a{background:var(--gold-dark)}
.cart{display:flex;align-items:center;gap:10px;background:var(--gold-dark);padding:0 28px;color:var(--white);font-size:11px;text-transform:uppercase;position:relative}
.cart-count{position:absolute;top:10px;right:20px;width:14px;height:14px;border-radius:50%;background:#d0021b;font-size:8px;display:flex;align-items:center;justify-content:center}

/* hero */
.hero{height:522px;background:var(--black);position:relative;overflow:hidden}
.hero-photo{position:absolute;right:0;top:0;width:520px;height:100%;background:radial-gradient(ellipse 60% 70% at 55% 45%,#c9a58c 0%,#8a6650 30%,#3a2a22 62%,#0d0d0d 100%)}
.hero-copy{position:absolute;left:160px;top:120px}
.hero-kicker{font-family:"Roboto Condensed",sans-serif;font-weight:700;font-size:44px;line-height:52px;color:var(--white);letter-spacing:.5px}
.hero-title{font-family:"Roboto Condensed",sans-serif;font-weight:700;font-size:55px;line-height:64px;color:var(--gold);margin-top:2px;letter-spacing:.5px}
.hero-text{font-size:14px;line-height:22px;color:var(--white);margin-top:12px;width:360px;text-transform:uppercase}
.hero-btn{display:flex;margin-top:36px;height:41px;width:152px;background:var(--gold)}
.hero-btn span{flex:1;display:flex;align-items:center;justify-content:center;font-size:10px;color:var(--white);text-transform:uppercase}
.hero-btn i{width:45px;background:var(--gold-dark);display:flex;align-items:center;justify-content:center}
.hero-arrow{position:absolute;top:242px;width:40px;height:40px;border:2px solid var(--gold);border-radius:50%;display:flex;align-items:center;justify-content:center}
.hero-arrow.prev{left:27px}
.hero-arrow.next{right:27px}
.hero-dots{position:absolute;left:568px;top:488px;display:flex;gap:4px}
.hero-dots span{width:18px;height:3px;background:var(--white)}

/* section titles */
.section-title{text-align:center;font-size:16px;font-weight:500;letter-spacing:1.5px;text-transform:uppercase;color:var(--ink)}
.title-rule{display:flex;justify-content:center;align-items:center;gap:6px;margin-top:12px}
.title-rule b{width:22px;height:1px;background:#999}
.title-rule i{width:22px;height:5px;background:var(--gold);transform:skewX(-45deg)}

/* product photo fills */
.ph-tracker{background:radial-gradient(ellipse 38% 48% at 32% 50%,#2c3230 0%,#3b403e 55%,rgba(0,0,0,0) 75%),radial-gradient(ellipse 18% 30% at 80% 38%,#3a3a3a 0%,rgba(0,0,0,0) 80%),linear-gradient(135deg,#f4f4f4,#d9d9d9)}
.ph-headphones{background:radial-gradient(ellipse 35% 40% at 45% 45%,#6a6a6a 0%,#2a2a2a 60%,#111 100%)}
.ph-band{background:radial-gradient(ellipse 45% 45% at 50% 45%,#1e1e1e 0%,#3a3a3a 60%,#8e8e8e 100%)}
.ph-camera{background:radial-gradient(ellipse 40% 42% at 48% 50%,#2a2a3e 0%,#4a3a4a 55%,#8a5a3a 100%)}
.ph-laptop{background:radial-gradient(ellipse 42% 38% at 50% 48%,#8b8f96 0%,#bfc2c6 55%,#f2f2f2 100%)}
.ph-tote{background:radial-gradient(ellipse 38% 38% at 50% 55%,#1e1e1e 0%,#2a2420 60%,rgba(0,0,0,0) 80%),#ececec}
.ph-player{background:radial-gradient(ellipse 40% 30% at 50% 48%,#c8b890 0%,#dcd6c4 60%,rgba(0,0,0,0) 85%),#f2f2f2}
.ph-coat{background:radial-gradient(ellipse 30% 50% at 50% 50%,#3e4630 0%,#4e5640 60%,rgba(0,0,0,0) 80%),#ececec}
.ph-silver{background:radial-gradient(ellipse 34% 34% at 48% 48%,#bdbdbd 0%,#dcdcdc 60%,rgba(0,0,0,0) 85%),#f5f5f5}
.ph-yellow{background:radial-gradient(ellipse 36% 38% at 50% 58%,#e8cf86 0%,#dcc89a 55%,rgba(0,0,0,0) 80%),#caa996}
.ph-watch{background:radial-gradient(ellipse 30% 44% at 48% 50%,#b89e94 0%,#cdb8b0 60%,rgba(0,0,0,0) 85%),#efefef}
.ph-luggage{background:radial-gradient(ellipse 38% 40% at 45% 55%,#4a3828 0%,#5a4530 55%,rgba(0,0,0,0) 80%),#f6f6f6}
.ph-rose{background:radial-gradient(ellipse 40% 36% at 50% 55%,#dcb29a 0%,#e8c8b4 60%,rgba(0,0,0,0) 85%),#f4f4f4}
.ph-phone{background:radial-gradient(ellipse 36% 50% at 55% 55%,#b3121a 0%,#8a0c12 60%,rgba(0,0,0,0) 80%),#f4f4f4}
.ph-tablet{background:radial-gradient(ellipse 40% 40% at 52% 52%,#1e1e1e 0%,#333 60%,rgba(0,0,0,0) 82%),#f4f4f4}

/* limited */
.limited{position:absolute;top:714px;left:160px;width:880px}
.limited-grid{position:relative;height:340px;margin-top:39px}
.tile{position:absolute;overflow:hidden}
.tile .photo{position:absolute;inset:0}
.tile-big{left:0;top:0;width:428px;height:340px}
.tile-a{left:450px;top:0;width:205px;height:159px}
.tile-b{left:675px;top:0;width:205px;height:159px}
.tile-c{left:450px;top:181px;width:205px;height:159px}
.tile-d{left:675px;top:181px;width:205px;height:159px}
.tile-tools{position:absolute;right:10px;top:10px;display:flex;flex-direction:column;gap:5px}
.tile-tools span{width:21px;height:21px;background:var(--gold);display:flex;align-items:center;justify-content:center}
.tile-band{position:absolute;left:0;right:0;bottom:0;height:30px;background:rgba(40,40,40,.78);display:flex;align-items:center;justify-content:space-between;padding:0 6px}
.tile-big .tile-band{height:52px;padding:0 14px}
.tile-name{font-size:10px;font-weight:700;color:var(--white);text-transform:uppercase;letter-spacing:.5px;line-height:12px;display:block}
.tile-price{font-size:10px;color:var(--white);display:block}
.tile-big .tile-name{font-size:13px;line-height:16px}
.tile-big .tile-price{font-size:11px}
.bid-btn{background:var(--gold);color:var(--white);font-size:9px;font-weight:500;text-transform:uppercase;padding:3px 6px}
.tile-big .bid-btn{font-size:11px;padding:7px 14px}

/* new products */
.new-products{position:absolute;top:1170px;left:160px;width:880px}
.product-grid{display:grid;grid-template-columns:repeat(5,168px);gap:12px 10px;margin-top:33px}
.card{border:1px solid var(--line);height:189px;background:var(--white)}
.card .photo{height:118px}
.card-bar{height:26px;background:#2e2e2e;display:flex;align-items:center}
.card-bar .bid{flex:1;text-align:center;color:var(--white);font-size:9px;font-weight:500;text-transform:uppercase}
.card-bar .ic{width:26px;height:26px;display:flex;align-items:center;justify-content:center}
.card-body{padding:8px 6px 0}
.card-title{font-size:10px;font-weight:500;color:#444;text-transform:uppercase;letter-spacing:.4px}
.card-price{font-size:10px;font-weight:700;color:var(--gold);margin-top:4px}

/* newsletter */
.newsletter{position:absolute;top:2062px;left:0;width:1200px;height:200px;background:var(--cream);text-align:center}
.newsletter h2{font-size:17px;font-weight:500;letter-spacing:.5px;text-transform:uppercase;color:#3a3a3a;margin-top:36px}
.newsletter p{font-size:11px;color:#666;margin-top:12px}
.subscribe{display:flex;width:582px;height:39px;margin:30px auto 0}
.subscribe input{flex:1;border:0;background:var(--white);padding:0 10px;font:11px "Roboto",sans-serif;color:#999}
.subscribe button{width:105px;border:0;background:var(--gold);color:var(--white);font:500 10px "Roboto",sans-serif;text-transform:uppercase;display:flex;align-items:center;justify-content:center;gap:8px}

/* footer */
.footer{position:absolute;top:2262px;left:0;width:1200px;height:273px;background:var(--footer);color:var(--footer-text)}
.footer-cols{position:absolute;left:160px;top:0;width:880px;height:210px}
.footer-col{position:absolute;top:0}
.footer-about{left:0;top:28px;width:200px}
.footer-about .brand{height:54px}
.footer-about .brand-name{color:#dcdcdc}
.footer-about p{font-size:10px;line-height:15px;margin-top:20px}
.footer-col h3{font-size:12px;font-weight:500;color:var(--white);text-transform:uppercase;letter-spacing:.5px;margin-top:47px}
.footer-col h3::after{content:"";display:block;width:26px;height:2px;background:var(--gold);margin-top:6px}
.footer-info{left:227px}
.footer-account{left:452px}
.footer-contact{left:675px;width:205px}
.footer-col ul{margin-top:22px}
.footer-col li{font-size:10px;line-height:12px;margin-bottom:13px;display:flex;align-items:flex-start;gap:18px}
.footer-col li::before{content:"";width:6px;height:6px;border-radius:50%;background:#dcdcdc;margin-top:3px;flex:none}
.footer-contact li::before{display:none}
.footer-contact li{gap:14px;line-height:15px;margin-bottom:12px}
.footer-contact svg{flex:none;margin-top:1px}
.footer-bottom{position:absolute;left:160px;top:218px;width:880px;border-top:1px solid #444;display:flex;justify-content:space-between;align-items:center;height:55px}
.footer-bottom p{font-size:10px}
.pay{display:flex;gap:10px}
.pay span{width:34px;height:22px;background:#d6d6d6;border-radius:2px;display:block}
</style>
</head>
<body>

<div class="topbar">
  <div class="social"><span></span><span></span><span></span><span></span></div>
  <nav class="account-links"><a href="#">Login</a><a href="#">Sign Up</a><a href="#">My Account</a><a href="#">Wishlist</a></nav>
</div>

<header class="header">
  <div class="brand"><span class="brand-dot"></span><span class="brand-name">lotvo</span></div>
  <form class="search">
    <input type="text" placeholder="Search for product">
    <button type="button" aria-label="Search">
      <svg width="16" height="16" viewBox="0 0 16 16"><circle cx="6.5" cy="6.5" r="5" fill="none" stroke="#fff" stroke-width="2"/><line x1="10.3" y1="10.3" x2="15" y2="15" stroke="#fff" stroke-width="2.4"/></svg>
    </button>
  </form>
</header>

<nav class="nav">
  <ul>
    <li class="active"><a href="#">Home</a></li>
    <li><a href="#">About Us</a></li>
    <li><a href="#">Products</a></li>
    <li><a href="#">Members</a></li>
    <li><a href="#">FAQ's</a></li>
    <li><a href="#">Contact Us</a></li>
  </ul>
  <a class="cart" href="#">Cart
    <svg width="18" height="15" viewBox="0 0 18 15"><path d="M1 2h3l2 8h9l2-6H5" fill="none" stroke="#fff" stroke-width="1.6"/><circle cx="7" cy="13" r="1.4" fill="#fff"/><circle cx="14" cy="13" r="1.4" fill="#fff"/></svg>
    <span class="cart-count">2</span>
  </a>
</nav>

<section class="hero">
  <div class="hero-photo" role="img" aria-label="Model wearing fine jewellery rings"></div>
  <div class="hero-copy">
    <p class="hero-kicker">OF LOREM IPSUM</p>
    <h1 class="hero-title">PREDEFINED SSARY</h1>
    <p class="hero-text">Shop from thousands of styles with up to 50% off in our huge end season sale!</p>
    <a class="hero-btn" href="#"><span>Grab it now</span><i><svg width="14" height="14" viewBox="0 0 14 14"><circle cx="7" cy="7" r="7" fill="#fff"/><path d="M6 4l3 3-3 3" fill="none" stroke="#9a8d68" stroke-width="1.6"/></svg></i></a>
  </div>
  <a class="hero-arrow prev" href="#" aria-label="Previous slide"><svg width="10" height="14" viewBox="0 0 10 14"><path d="M8 1L2 7l6 6" fill="none" stroke="#ab9e78" stroke-width="2"/></svg></a>
  <a class="hero-arrow next" href="#" aria-label="Next slide"><svg width="10" height="14" viewBox="0 0 10 14"><path d="M2 1l6 6-6 6" fill="none" stroke="#ab9e78" stroke-width="2"/></svg></a>
  <div class="hero-dots"><span></span><span></span><span></span></div>
</section>

<section class="limited">
  <h2 class="section-title">Limited Edition Products</h2>
  <div class="title-rule"><b></b><i></i><b></b></div>
  <div class="limited-grid">
    <article class="tile tile-big">
      <div class="photo ph-tracker" role="img" aria-label="Black fitness tracker watch"></div>
      <div class="tile-tools">
        <span><svg width="11" height="10" viewBox="0 0 12 11"><path d="M6 10L1.5 5.5A2.6 2.6 0 016 2a2.6 2.6 0 014.5 3.5z" fill="none" stroke="#fff" stroke-width="1.3"/></svg></span>
        <span><svg width="12" height="8" viewBox="0 0 12 8"><path d="M1 4c2-4 8-4 10 0-2 4-8 4-10 0z" fill="#fff"/><circle cx="6" cy="4" r="1.5" fill="#ab9e78"/></svg></span>
        <span><svg width="11" height="11" viewBox="0 0 11 11"><line x1="5" y1="5" x2="1" y2="10" stroke="#fff" stroke-width="1.6"/><rect x="5" y="1" width="5" height="3" fill="#fff"/></svg></span>
      </div>
      <div class="tile-band"><div><span class="tile-name">Product Title</span><span class="tile-price">$1200.00</span></div><span class="bid-btn">Bid Now</span></div>
    </article>
    <article class="tile tile-a">
      <div class="photo ph-headphones" role="img" aria-label="Black in-ear headphones"></div>
      <div class="tile-tools"><span><svg width="10" height="9" viewBox="0 0 12 11"><path d="M6 10L1.5 5.5A2.6 2.6 0 016 2a2.6 2.6 0 014.5 3.5z" fill="none" stroke="#fff" stroke-width="1.3"/></svg></span><span><svg width="11" height="7" viewBox="0 0 12 8"><path d="M1 4c2-4 8-4 10 0-2 4-8 4-10 0z" fill="#fff"/></svg></span><span><svg width="10" height="10" viewBox="0 0 11 11"><line x1="5" y1="5" x2="1" y2="10" stroke="#fff" stroke-width="1.6"/><rect x="5" y="1" width="5" height="3" fill="#fff"/></svg></span></div>
      <div class="tile-band"><div><span class="tile-name">Product Title</span><span class="tile-price">$900.00</span></div><span class="bid-btn">Bid Now</span></div>
    </article>
    <article class="tile tile-b">
      <div class="photo ph-band" role="img" aria-label="Digital wrist band"></div>
      <div class="tile-tools"><span><svg width="10" height="9" viewBox="0 0 12 11"><path d="M6 10L1.5 5.5A2.6 2.6 0 016 2a2.6 2.6 0 014.5 3.5z" fill="none" stroke="#fff" stroke-width="1.3"/></svg></span><span><svg width="11" height="7" viewBox="0 0 12 8"><path d="M1 4c2-4 8-4 10 0-2 4-8 4-10 0z" fill="#fff"/></svg></span><span><svg width="10" height="10" viewBox="0 0 11 11"><line x1="5" y1="5" x2="1" y2="10" stroke="#fff" stroke-width="1.6"/><rect x="5" y="1" width="5" height="3" fill="#fff"/></svg></span></div>
      <div class="tile-band"><div><span class="tile-name">Product Title</span><span class="tile-price">$750.00</span></div><span class="bid-btn">Bid Now</span></div>
    </article>
    <article class="tile tile-c">
      <div class="photo ph-camera" role="img" aria-label="Compact camera on a wooden table"></div>
      <div class="tile-tools"><span><svg width="10" height="9" viewBox="0 0 12 11"><path d="M6 10L1.5 5.5A2.6 2.6 0 016 2a2.6 2.6 0 014.5 3.5z" fill="none" stroke="#fff" stroke-width="1.3"/></svg></span><span><svg width="11" height="7" viewBox="0 0 12 8"><path d="M1 4c2-4 8-4 10 0-2 4-8 4-10 0z" fill="#fff"/></svg></span><span><svg width="10" height="10" viewBox="0 0 11 11"><line x1="5" y1="5" x2="1" y2="10" stroke="#fff" stroke-width="1.6"/><rect x="5" y="1" width="5" height="3" fill="#fff"/></svg></span></div>
      <div class="tile-band"><div><span class="tile-name">Product Title</span><span class="tile-price">$600.00</span></div><span class="bid-btn">Bid Now</span></div>
    </article>
    <article class="tile tile-d">
      <div class="photo ph-laptop" role="img" aria-label="Laptop on a desk"></div>
      <div class="tile-tools"><span><svg width="10" height="9" viewBox="0 0 12 11"><path d="M6 10L1.5 5.5A2.6 2.6 0 016 2a2.6 2.6 0 014.5 3.5z" fill="none" stroke="#fff" stroke-width="1.3"/></svg></span><span><svg width="11" height="7" viewBox="0 0 12 8"><path d="M1 4c2-4 8-4 10 0-2 4-8 4-10 0z" fill="#fff"/></svg></span><span><svg width="10" height="10" viewBox="0 0 11 11"><line x1="5" y1="5" x2="1" y2="10" stroke="#fff" stroke-width="1.6"/><rect x="5" y="1" width="5" height="3" fill="#fff"/></svg></span></div>
      <div class="tile-band"><div><span class="tile-name">Product Title</span><span class="tile-price">$500.00</span></div><span class="bid-btn">Bid Now</span></div>
    </article>
  </div>
</section>

<section class="new-products">
  <h2 class="section-title">Shop That New Products</h2>
  <div class="title-rule"><b></b><i></i><b></b></div>
  <div class="product-grid">
    <article class="card"><div class="photo ph-tote" role="img" aria-label="Black leather tote bag"></div><div class="card-bar"><span class="bid">Bid Now</span><span class="ic"><svg width="10" height="9" viewBox="0 0 12 11"><path d="M6 10.5L1 5.5A2.8 2.8 0 016 1.8a2.8 2.8 0 015 3.7z" fill="#fff"/></svg></span><span class="ic"><svg width="11" height="7" viewBox="0 0 12 8"><path d="M1 4c2-4 8-4 10 0-2 4-8 4-10 0z" fill="#fff"/></svg></span></div><div class="card-body"><h3 class="card-title">Sample Product Title</h3><p class="card-price">$1000.00</p></div></article>
    <article class="card"><div class="photo ph-player" role="img" aria-label="Silver music player with earphones"></div><div class="card-bar"><span class="bid">Bid Now</span><span class="ic"><svg width="10" height="9" viewBox="0 0 12 11"><path d="M6 10.5L1 5.5A2.8 2.8 0 016 1.8a2.8 2.8 0 015 3.7z" fill="#fff"/></svg></span><span class="ic"><svg width="11" height="7" viewBox="0 0 12 8"><path d="M1 4c2-4 8-4 10 0-2 4-8 4-10 0z" fill="#fff"/></svg></span></div><div class="card-body"><h3 class="card-title">Sample Product Title</h3><p class="card-price">$1000.00</p></div></article>
    <article class="card"><div class="photo ph-coat" role="img" aria-label="Dark green wool coat"></div><div class="card-bar"><span class="bid">Bid Now</span><span class="ic"><svg width="10" height="9" viewBox="0 0 12 11"><path d="M6 10.5L1 5.5A2.8 2.8 0 016 1.8a2.8 2.8 0 015 3.7z" fill="#fff"/></svg></span><span class="ic"><svg width="11" height="7" viewBox="0 0 12 8"><path d="M1 4c2-4 8-4 10 0-2 4-8 4-10 0z" fill="#fff"/></svg></span></div><div class="card-body"><h3 class="card-title">Sample Product Title</h3><p class="card-price">$1000.00</p></div></article>
    <article class="card"><div class="photo ph-silver" role="img" aria-label="Silver compact music player"></div><div class="card-bar"><span class="bid">Bid Now</span><span class="ic"><svg width="10" height="9" viewBox="0 0 12 11"><path d="M6 10.5L1 5.5A2.8 2.8 0 016 1.8a2.8 2.8 0 015 3.7z" fill="#fff"/></svg></span><span class="ic"><svg width="11" height="7" viewBox="0 0 12 8"><path d="M1 4c2-4 8-4 10 0-2 4-8 4-10 0z" fill="#fff"/></svg></span></div><div class="card-body"><h3 class="card-title">Sample Product Title</h3><p class="card-price">$1000.00</p></div></article>
    <article class="card"><div class="photo ph-yellow" role="img" aria-label="Yellow leather handbag"></div><div class="card-bar"><span class="bid">Bid Now</span><span class="ic"><svg width="10" height="9" viewBox="0 0 12 11"><path d="M6 10.5L1 5.5A2.8 2.8 0 016 1.8a2.8 2.8 0 015 3.7z" fill="#fff"/></svg></span><span class="ic"><svg width="11" height="7" viewBox="0 0 12 8"><path d="M1 4c2-4 8-4 10 0-2 4-8 4-10 0z" fill="#fff"/></svg></span></div><div class="card-body"><h3 class="card-title">Sample Product Title</h3><p class="card-price">$1000.00</p></div></article>

    <article class="card"><div class="photo ph-watch" role="img" aria-label="Smart watch with pink strap"></div><div class="card-bar"><span class="bid">Bid Now</span><span class="ic"><svg width="10" height="9" viewBox="0 0 12 11"><path d="M6 10.5L1 5.5A2.8 2.8 0 016 1.8a2.8 2.8 0 015 3.7z" fill="#fff"/></svg></span><span class="ic"><svg width="11" height="7" viewBox="0 0 12 8"><path d="M1 4c2-4 8-4 10 0-2 4-8 4-10 0z" fill="#fff"/></svg></span></div><div class="card-body"><h3 class="card-title">Sample Product Title</h3><p class="card-price">$1000.00</p></div></article>
    <article class="card"><div class="photo ph-luggage" role="img" aria-label="Patterned rolling luggage"></div><div class="card-bar"><span class="bid">Bid Now</span><span class="ic"><svg width="10" height="9" viewBox="0 0 12 11"><path d="M6 10.5L1 5.5A2.8 2.8 0 016 1.8a2.8 2.8 0 015 3.7z" fill="#fff"/></svg></span><span class="ic"><svg width="11" height="7" viewBox="0 0 12 8"><path d="M1 4c2-4 8-4 10 0-2 4-8 4-10 0z" fill="#fff"/></svg></span></div><div class="card-body"><h3 class="card-title">Sample Product Title</h3><p class="card-price">$1000.00</p></div></article>
    <article class="card"><div class="photo ph-rose" role="img" aria-label="Rose gold leather bag"></div><div class="card-bar"><span class="bid">Bid Now</span><span class="ic"><svg width="10" height="9" viewBox="0 0 12 11"><path d="M6 10.5L1 5.5A2.8 2.8 0 016 1.8a2.8 2.8 0 015 3.7z" fill="#fff"/></svg></span><span class="ic"><svg width="11" height="7" viewBox="0 0 12 8"><path d="M1 4c2-4 8-4 10 0-2 4-8 4-10 0z" fill="#fff"/></svg></span></div><div class="card-body"><h3 class="card-title">Sample Product Title</h3><p class="card-price">$1000.00</p></div></article>
    <article class="card"><div class="photo ph-phone" role="img" aria-label="Red smartphone"></div><div class="card-bar"><span class="bid">Bid Now</span><span class="ic"><svg width="10" height="9" viewBox="0 0 12 11"><path d="M6 10.5L1 5.5A2.8 2.8 0 016 1.8a2.8 2.8 0 015 3.7z" fill="#fff"/></svg></span><span class="ic"><svg width="11" height="7" viewBox="0 0 12 8"><path d="M1 4c2-4 8-4 10 0-2 4-8 4-10 0z" fill="#fff"/></svg></span></div><div class="card-body"><h3 class="card-title">Sample Product Title</h3><p class="card-price">$1000.00</p></div></article>
    <article class="card"><div class="photo ph-tablet" role="img" aria-label="Tablet with keyboard case"></div><div class="card-bar"><span class="bid">Bid Now</span><span class="ic"><svg width="10" height="9" viewBox="0 0 12 11"><path d="M6 10.5L1 5.5A2.8 2.8 0 016 1.8a2.8 2.8 0 015 3.7z" fill="#fff"/></svg></span><span class="ic"><svg width="11" height="7" viewBox="0 0 12 8"><path d="M1 4c2-4 8-4 10 0-2 4-8 4-10 0z" fill="#fff"/></svg></span></div><div class="card-body"><h3 class="card-title">Sample Product Title</h3><p class="card-price">$1000.00</p></div></article>

    <article class="card"><div class="photo ph-tote" role="img" aria-label="Black leather tote bag"></div><div class="card-bar"><span class="bid">Bid Now</span><span class="ic"><svg width="10" height="9" viewBox="0 0 12 11"><path d="M6 10.5L1 5.5A2.8 2.8 0 016 1.8a2.8 2.8 0 015 3.7z" fill="#fff"/></svg></span><span class="ic"><svg width="11" height="7" viewBox="0 0 12 8"><path d="M1 4c2-4 8-4 10 0-2 4-8 4-10 0z" fill="#fff"/></svg></span></div><div class="card-body"><h3 class="card-title">Sample Product Title</h3><p class="card-price">$1000.00</p></div></article>
    <article class="card"><div class="photo ph-player" role="img" aria-label="Silver music player with earphones"></div><div class="card-bar"><span class="bid">Bid Now</span><span class="ic"><svg width="10" height="9" viewBox="0 0 12 11"><path d="M6 10.5L1 5.5A2.8 2.8 0 016 1.8a2.8 2.8 0 015 3.7z" fill="#fff"/></svg></span><span class="ic"><svg width="11" height="7" viewBox="0 0 12 8"><path d="M1 4c2-4 8-4 10 0-2 4-8 4-10 0z" fill="#fff"/></svg></span></div><div class="card-body"><h3 class="card-title">Sample Product Title</h3><p class="card-price">$1000.00</p></div></article>
    <article class="card"><div class="photo ph-coat" role="img" aria-label="Dark green wool coat"></div><div class="card-bar"><span class="bid">Bid Now</span><span class="ic"><svg width="10" height="9" viewBox="0 0 12 11"><path d="M6 10.5L1 5.5A2.8 2.8 0 016 1.8a2.8 2.8 0 015 3.7z" fill="#fff"/></svg></span><span class="ic"><svg width="11" height="7" viewBox="0 0 12 8"><path d="M1 4c2-4 8-4 10 0-2 4-8 4-10 0z" fill="#fff"/></svg></span></div><div class="card-body"><h3 class="card-title">Sample Product Title</h3><p class="card-price">$1000.00</p></div></article>
    <article class="card"><div class="photo ph-silver" role="img" aria-label="Silver compact music player"></div><div class="card-bar"><span class="bid">Bid Now</span><span class="ic"><svg width="10" height="9" viewBox="0 0 12 11"><path d="M6 10.5L1 5.5A2.8 2.8 0 016 1.8a2.8 2.8 0 015 3.7z" fill="#fff"/></svg></span><span class="ic"><svg width="11" height="7" viewBox="0 0 12 8"><path d="M1 4c2-4 8-4 10 0-2 4-8 4-10 0z" fill="#fff"/></svg></span></div><div class="card-body"><h3 class="card-title">Sample Product Title</h3><p class="card-price">$1000.00</p></div></article>
    <article class="card"><div class="photo ph-yellow" role="img" aria-label="Yellow leather handbag"></div><div class="card-bar"><span class="bid">Bid Now</span><span class="ic"><svg width="10" height="9" viewBox="0 0 12 11"><path d="M6 10.5L1 5.5A2.8 2.8 0 016 1.8a2.8 2.8 0 015 3.7z" fill="#fff"/></svg></span><span class="ic"><svg width="11" height="7" viewBox="0 0 12 8"><path d="M1 4c2-4 8-4 10 0-2 4-8 4-10 0z" fill="#fff"/></svg></span></div><div class="card-body"><h3 class="card-title">Sample Product Title</h3><p class="card-price">$1000.00</p></div></article>

    <article class="card"><div class="photo ph-watch" role="img" aria-label="Smart watch with pink strap"></div><div class="card-bar"><span class="bid">Bid Now</span><span class="ic"><svg width="10" height="9" viewBox="0 0 12 11"><path d="M6 10.5L1 5.5A2.8 2.8 0 016 1.8a2.8 2.8 0 015 3.7z" fill="#fff"/></svg></span><span class="ic"><svg width="11" height="7" viewBox="0 0 12 8"><path d="M1 4c2-4 8-4 10 0-2 4-8 4-10 0z" fill="#fff"/></svg></span></div><div class="card-body"><h3 class="card-title">Sample Product Title</h3><p class="card-price">$1000.00</p></div></article>
    <article class="card"><div class="photo ph-luggage" role="img" aria-label="Patterned rolling luggage"></div><div class="card-bar"><span class="bid">Bid Now</span><span class="ic"><svg width="10" height="9" viewBox="0 0 12 11"><path d="M6 10.5L1 5.5A2.8 2.8 0 016 1.8a2.8 2.8 0 015 3.7z" fill="#fff"/></svg></span><span class="ic"><svg width="11" height="7" viewBox="0 0 12 8"><path d="M1 4c2-4 8-4 10 0-2 4-8 4-10 0z" fill="#fff"/></svg></span></div><div class="card-body"><h3 class="card-title">Sample Product Title</h3><p class="card-price">$1000.00</p></div></article>
    <article class="card"><div class="photo ph-rose" role="img" aria-label="Rose gold leather bag"></div><div class="card-bar"><span class="bid">Bid Now</span><span class="ic"><svg width="10" height="9" viewBox="0 0 12 11"><path d="M6 10.5L1 5.5A2.8 2.8 0 016 1.8a2.8 2.8 0 015 3.7z" fill="#fff"/></svg></span><span class="ic"><svg width="11" height="7" viewBox="0 0 12 8"><path d="M1 4c2-4 8-4 10 0-2 4-8 4-10 0z" fill="#fff"/></svg></span></div><div class="card-body"><h3 class="card-title">Sample Product Title</h3><p class="card-price">$1000.00</p></div></article>
    <article class="card"><div class="photo ph-phone" role="img" aria-label="Red smartphone"></div><div class="card-bar"><span class="bid">Bid Now</span><span class="ic"><svg width="10" height="9" viewBox="0 0 12 11"><path d="M6 10.5L1 5.5A2.8 2.8 0 016 1.8a2.8 2.8 0 015 3.7z" fill="#fff"/></svg></span><span class="ic"><svg width="11" height="7" viewBox="0 0 12 8"><path d="M1 4c2-4 8-4 10 0-2 4-8 4-10 0z" fill="#fff"/></svg></span></div><div class="card-body"><h3 class="card-title">Sample Product Title</h3><p class="card-price">$1000.00</p></div></article>
    <article class="card"><div class="photo ph-tablet" role="img" aria-label="Tablet with keyboard case"></div><div class="card-bar"><span class="bid">Bid Now</span><span class="ic"><svg width="10" height="9" viewBox="0 0 12 11"><path d="M6 10.5L1 5.5A2.8 2.8 0 016 1.8a2.8 2.8 0 015 3.7z" fill="#fff"/></svg></span><span class="ic"><svg width="11" height="7" viewBox="0 0 12 8"><path d="M1 4c2-4 8-4 10 0-2 4-8 4-10 0z" fill="#fff"/></svg></span></div><div class="card-body"><h3 class="card-title">Sample Product Title</h3><p class="card-price">$1000.00</p></div></article>
  </div>
</section>

<section class="newsletter">
  <h2>Subscribe to Newsletter</h2>
  <p>Contrary to popular belief, Lorem Ipsum is not simply random text</p>
  <form class="subscribe">
    <input type="email" placeholder="Enter your email">
    <button type="button"><svg width="11" height="8" viewBox="0 0 11 8"><rect x=".5" y=".5" width="10" height="7" fill="none" stroke="#fff"/><path d="M.5 .5l5 4 5-4" fill="none" stroke="#fff"/></svg>Subscribe</button>
  </form>
</section>

<footer class="footer">
  <div class="footer-cols">
    <div class="footer-col footer-about">
      <div class="brand"><span class="brand-dot"></span><span class="brand-name">lotvo</span></div>
      <p>There are many variations of passages of Lorem Ipsum available, but the majority have suffered alteration in some form, by injected humour, or randomised words which don't look even slightly believable.</p>
    </div>
    <div class="footer-col footer-info">
      <h3>Information</h3>
      <ul><li>My Account</li><li>Order History</li><li>Contact Us</li><li>Terms &amp; Condition</li></ul>
    </div>
    <div class="footer-col footer-account">
      <h3>My Account</h3>
      <ul><li>Privacy Policya</li><li>Delivery Information</li><li>Manufacturers</li><li>Site Map</li></ul>
    </div>
    <div class="footer-col footer-contact">
      <h3>Get in Touch</h3>
      <ul>
        <li><svg width="9" height="12" viewBox="0 0 9 12"><path d="M4.5 12S0 7 0 4.5a4.5 4.5 0 019 0C9 7 4.5 12 4.5 12z" fill="#dcdcdc"/><circle cx="4.5" cy="4.5" r="1.6" fill="#2c2c2c"/></svg>There are many variations of passages of Lorem Ipsum available</li>
        <li><svg width="11" height="11" viewBox="0 0 11 11"><path d="M2 0l2 2.5-1.2 1.5a7 7 0 004.2 4.2L8.5 7 11 9l-1.5 2C4.5 11 0 6.5 0 1.5z" fill="#dcdcdc"/></svg>(+1)555-014-2290</li>
        <li><svg width="12" height="9" viewBox="0 0 12 9"><rect x=".5" y=".5" width="11" height="8" fill="none" stroke="#dcdcdc"/><path d="M.5 .5l5.5 4.5 5.5-4.5" fill="none" stroke="#dcdcdc"/></svg>info@lotvo.example</li>
      </ul>
    </div>
  </div>
  <div class="footer-bottom">
    <p>Copyright © 2017 lotvo. All rights reserved.</p>
    <div class="pay"><span></span><span></span><span></span><span></span><span></span></div>
  </div>
</footer>

</body>
</html>
```